We need a flyer where we promote a workshop to our members of the jewish community www.vbq-gemeinde.example . The workshop is calles "command in seven weeks presented by VBQ. We would like to see a flyer with the below text is used and also some pictures (attached). The flyer should come over as cool, fresh, innovative for a younger crowd so called young professionals (age 28-35).
TITLE.
"Command in Seven Weeks.
SUBTITLE.
Your systematic self-coaching roadmap to power and impact—and your future.”
TEXT.
Dr. Marcus L. Brandauer is the CEO Emeritus of Alpine Advisory Partners—he made an exit in 2013. He is the award-winning author of 8 books, including "Momentum-By-Design," "Speak Up or Fade" and "The Cantor and the Chairman.”
For the past 20 years he has taught leadership at Harwick University in New York and at KLB (Lindmoor University) to prepare future CEOs and other leaders in business, government , nonprofits and the military.
Now, in a process exclusively designed for VBQ’s next generation of emerging leaders, Marcus unpacks his leadership secrets in 3 action-packed labs—reduced to the max:
Lab 1. Command in Seven Weeks: The Summit Compass Model®. Self-Assessment. Self-Leadership: “The Lantern.” 5-Year Vision. 100-Day Catalytic Project.
Lab 2. Guiding Through Words. Relationship: Building Trust. Momentum-By-Design. Cockpit.
Lab 3. Debrief and Scale-Up. Sustainability. Action Tools.
Do you want to build your own future and a life you love? Do you want to jump-start that future and life over 100 days while learning a toolbox of leadership skills, networking with like-minded people—and even get some pizza? Then join us.
young professionals age 28-35

```html
<!DOCTYPE html>
<html lang="en">
<head>
<meta charset="utf-8">
<title>Command in Seven Weeks – Workshop Flyer</title>
<link rel="stylesheet" href="https://fonts.googleapis.com/css2?family=Michroma&family=Oswald:wght@500;600&family=Roboto+Condensed:wght@700&family=Roboto:ital,wght@0,300;0,400;0,500;1,300;1,700&display=swap">
<style>
  :root {
    --page-bg: #e4e5e7;
    --sky-top: #3aa3e6;
    --sky-mid: #1f6fc4;
    --navy: #141c5a;
    --navy-deep: #10174d;
    --band: #3d5fd0;
    --ink: #0b0b14;
    --white: #ffffff;
    --teal: #62d3d1;
    --tag: #3f8fc8;
    --rule: #4f6aa8;
  }
  * { box-sizing: border-box; margin: 0; padding: 0; }
  html, body { width: 1200px; height: 1200px; overflow: hidden; background: var(--page-bg); }
  .flyer {
    position: absolute; left: 136px; top: 0; width: 927px; height: 1200px; overflow: hidden;
    background: linear-gradient(180deg, var(--sky-top) 0%, var(--sky-mid) 22%, #1b3f8f 36%, #0f1a45 50%, var(--navy) 68%, var(--navy-deep) 100%);
    color: var(--white); font-family: "Roboto", sans-serif;
  }
  .side-band { position: absolute; left: 72px; top: 0; width: 58px; height: 640px;
    background: linear-gradient(180deg, rgba(61,95,208,.55), rgba(61,95,208,.9) 55%, rgba(61,95,208,0)); }
  .stage-photo { position: absolute; left: 0; top: 400px; width: 927px; height: 400px;
    background: radial-gradient(ellipse 60% 55% at 55% 45%, #2d3f8c 0%, #1a2466 45%, rgba(20,28,90,0) 80%),
                linear-gradient(180deg, rgba(15,26,69,0) 0%, #17205e 30%, #1b2a72 70%, rgba(20,28,90,0) 100%); }
  .portrait { position: absolute; left: 70px; top: 624px; width: 114px; height: 140px;
    background: linear-gradient(160deg, #9fc3dc, #5e7190 60%, #3b4660); }
  .subtitle { position: absolute; left: 144px; top: 75px; font-family: "Roboto Condensed", sans-serif;
    font-weight: 700; font-size: 19.5px; color: var(--ink); white-space: nowrap; }
  .headline { position: absolute; left: 0; top: 0; }
  .headline .main { font-family: "Oswald", sans-serif; font-weight: 600; fill: var(--white); }
  .headline .wide { font-family: "Michroma", sans-serif; fill: var(--white); }
  .presenter { position: absolute; left: 0; width: 927px; top: 391px; text-align: center;
    font-family: "Michroma", sans-serif; font-size: 25px; letter-spacing: .5px; }
  .bio { position: absolute; left: 71px; top: 782px; width: 820px; font-size: 13.4px; line-height: 16.4px; }
  .bio p + p { margin-top: 17px; }
  .bio .name { font-weight: 700; font-style: italic; font-size: 15px; }
  .labs { position: absolute; left: 71px; top: 925px; width: 820px; list-style: none; }
  .lab { display: flex; align-items: flex-start; font-size: 15.5px; line-height: 20px; margin-bottom: 10px; }
  .lab:nth-child(2) { margin-bottom: 20px; }
  .lab-tag { flex: none; width: 57px; height: 25px; margin-right: 11px; margin-top: -1px;
    background: var(--tag); color: #0d1a3e; font-size: 13px; font-weight: 500; line-height: 25px; padding-left: 6px;
    clip-path: polygon(0 0, 82% 0, 100% 50%, 82% 100%, 0 100%); }
  .pitch { position: absolute; left: 71px; top: 1052px; width: 820px; font-size: 16px; line-height: 20px; }
  .pitch .question { color: var(--teal); font-weight: 500; font-size: 17px; }
  .join { position: absolute; left: 72px; top: 1133px; width: 814px; display: flex; align-items: center; }
  .join-label { font-size: 21px; font-weight: 400; white-space: nowrap; }
  .join-rule { flex: 1; height: 1px; background: var(--rule); margin: 2px 12px 0; }
  .join-url { font-size: 19px; font-weight: 300; font-style: italic; letter-spacing: 2.5px; white-space: nowrap; }
</style>
</head>
<body>
<main class="flyer">
  <div class="side-band"></div>
  <div class="stage-photo" role="img" aria-label="Photo of a speaker on a conference stage before a large audience, with screens behind him"></div>

  <p class="subtitle">Your systematic self-coaching roadmap to power and impact-and your future.</p>

  <svg class="headline" width="927" height="390" viewBox="0 0 927 390" aria-label="Command in Seven Weeks">
    <text class="main" x="144" y="247" font-size="176" textLength="572" lengthAdjust="spacingAndGlyphs">COMMAND</text>
    <text class="main" x="144" y="362" font-size="74" textLength="50" lengthAdjust="spacingAndGlyphs">IN</text>
    <text class="wide" x="222" y="362" font-size="74" textLength="636" lengthAdjust="spacingAndGlyphs">SEVEN WEEKS</text>
  </svg>

  <p class="presenter">Dr. Marcus L. Brandauer</p>

  <div class="portrait" role="img" aria-label="Portrait photo of Dr. Marcus L. Brandauer in a suit"></div>

  <section class="bio">
    <p><span class="name">Dr. Marcus L. Brandauer</span> is the CEO Emeritus of Alpine Advisory Partners—he made an exit in 2013.<br>He is the award-winning author of 8 books, including "Momentum-By-Design," "Speak Up or Fade" and "The Cantor and the Chairman."</p>
    <p>For the past 20 years he has taught leadership at Harwick University in New York and at KLB (Lindmoor University) to prepare future CEOs and other leaders in business, government , nonprofits and the military.</p>
    <p>Now, in a process exclusively designed for VBQ’s next generation of emerging leaders, Marcus unpacks his leadership secrets in 3 action-packed labs—reduced to the max:</p>
  </section>

  <ul class="labs">
    <li class="lab"><span class="lab-tag">Lab 1.</span><span>Command in Seven Weeks: The Summit Compass Model®. Self-Assessment.<br>Self-Leadership: “The Lantern.” 5-Year Vision. 100-Day Catalytic Project.</span></li>
    <li class="lab"><span class="lab-tag">Lab 2.</span><span>Guiding Through Words. Relationship: Building Trust. Momentum-By-Design. Cockpit.</span></li>
    <li class="lab"><span class="lab-tag">Lab 3.</span><span>Debrief and Scale-Up. Sustainability. Action Tools.</span></li>
  </ul>

  <section class="pitch">
    <p class="question">Do you want to build your own future and a life you love?</p>
    <p>Do you want to jump-start that future and life over 100 days while learning a toolbox of leadership skills, networking with like-minded people—and even get some pizza?</p>
  </section>

  <div class="join">
    <span class="join-label">Then join us.</span>
    <span class="join-rule"></span>
    <span class="join-url">www.vbq-gemeinde.example</span>
  </div>
</main>
</body>
</html>
```